Email signature and business card

Australian company called Tarrowin. We provide construction and maintenance services to the mining industry. I would like the design to be similar to our website theme(www.tarrowin.com.au) whilst staying compact. RGB colours to include: 42,96,140 and 232,163,0 and I have attached 2 logos.

The following fields will need to be included:

Full Name
Title
Location/Project
Phone
Mobile
Fax
Email
Web site

Target Market(s)

Mining Industry

Industry/Entity Type

Construction

Requirements
Must have
• Full Name, Title, Office Address, Phone, Mobile, Fax, Email, Web address
• Back of card must include: Boilermaking, Carpentry, Concrete, Construction, Cranes, Data and Comms, Electrical, Fabrication, Fitting, Labour Hire, Plumbing, Rigging, Shutdowns

```html
<!DOCTYPE html>
<html lang="en">
<head>
<meta charset="utf-8">
<title>Tarrowin Stationery</title>
<link rel="stylesheet" href="https://fonts.googleapis.com/css2?family=Mulish:wght@400;600;800&display=swap">
<style>
  :root {
    --brand-blue: #0c5a80;
    --card-blue: #2a608c;
    --brand-yellow: #e8a300;
    --ink: #3a3a3a;
    --paper: #ffffff;
    --envelope-inner: #f1f1f1;
    --backdrop: #8c8c8c;
  }
  * { box-sizing: border-box; margin: 0; padding: 0; }
  html, body { width: 1200px; height: 800px; overflow: hidden; }
  body {
    background: var(--backdrop);
    font-family: "Mulish", sans-serif;
    color: var(--ink);
    position: relative;
  }
  .piece { position: absolute; background: var(--paper); }

  /* brand lockup */
  .brand { display: flex; align-items: center; gap: 6px; }
  .brand-dot { border-radius: 50%; background: var(--brand-blue); flex: none; }
  .brand-name { font-weight: 800; color: var(--brand-blue); letter-spacing: 0.02em; }

  /* footer band with web tab */
  .band {
    position: absolute; left: 0; right: 0; bottom: 0;
    height: 5px; background: var(--brand-blue);
  }
  .web-tab {
    position: absolute; bottom: 5px;
    background: var(--brand-yellow); color: var(--paper);
    font-weight: 600; text-align: center;
    clip-path: polygon(6% 0, 94% 0, 100% 100%, 0 100%);
  }

  /* envelope back */
  .envelope-back {
    left: 80px; top: 40px; width: 460px; height: 290px;
    background: var(--envelope-inner);
    border-radius: 10px 10px 0 0;
  }
  .envelope-flap {
    position: absolute; left: 142px; top: 187px; width: 460px; height: 90px;
    background: var(--brand-blue);
    border-radius: 0 0 12px 12px;
  }

  /* envelope front */
  .envelope-front { left: 88px; top: 326px; width: 452px; height: 240px; }
  .envelope-front .brand { position: absolute; left: 20px; top: 30px; }
  .envelope-front .brand-dot { width: 36px; height: 36px; }
  .envelope-front .brand-name { font-size: 17px; }
  .envelope-front .address {
    position: absolute; left: 60px; top: 66px; font-size: 8px; line-height: 1.3;
  }
  .envelope-front .web-tab { left: 64px; width: 84px; height: 10px; font-size: 6px; line-height: 10px; }

  /* letterhead */
  .letterhead { left: 650px; top: 80px; width: 486px; height: 596px; }
  .letterhead .brand { position: absolute; left: 97px; top: 36px; }
  .letterhead .brand-dot { width: 40px; height: 40px; }
  .letterhead .brand-name { font-size: 20px; }
  .letterhead .contact {
    position: absolute; left: 36px; top: 566px; font-size: 7px; line-height: 1.35;
  }
  .letterhead .contact b { font-weight: 800; }
  .letterhead .web-tab { right: 90px; width: 86px; height: 11px; font-size: 6px; line-height: 11px; }

  /* business card front */
  .card-front { left: 122px; top: 626px; width: 190px; height: 107px; }
  .card-front .holder { position: absolute; left: 12px; top: 16px; }
  .card-front .holder-name { font-size: 7px; font-weight: 800; color: var(--brand-blue); }
  .card-front .holder-title { font-size: 5px; }
  .card-front .brand { position: absolute; right: 10px; top: 12px; gap: 4px; }
  .card-front .brand-dot { width: 24px; height: 24px; }
  .card-front .brand-name { font-size: 11px; }
  .card-front .details {
    position: absolute; left: 12px; top: 55px; font-size: 4.2px; line-height: 1.35;
  }
  .card-front .details .gap { height: 3px; }
  .card-front .web-tab { right: 10px; width: 60px; height: 7px; font-size: 4px; line-height: 7px; }
  .card-front .band { height: 3px; }

  /* business card back */
  .card-back {
    left: 335px; top: 628px; width: 190px; height: 106px;
    background: var(--card-blue); color: var(--paper);
  }
  .card-back .brand { position: absolute; left: 12px; top: 14px; gap: 4px; }
  .card-back .brand-dot { width: 22px; height: 22px; background: var(--paper); }
  .card-back .brand-name { font-size: 11px; color: var(--paper); }
  .services {
    position: absolute; left: 12px; top: 74px;
    display: flex; list-style: none;
  }
  .services ul { list-style: none; font-size: 4.4px; line-height: 1.45; padding: 0 6px; }
  .services ul:first-child { padding-left: 0; }
  .services ul + ul { border-left: 0.6px solid var(--brand-yellow); }
</style>
</head>
<body>

  <div class="piece envelope-back"></div>
  <div class="envelope-flap"></div>

  <section class="piece envelope-front">
    <div class="brand">
      <span class="brand-dot"></span>
      <span class="brand-name">TARROWIN</span>
    </div>
    <p class="address">Level 3, 14 Harbourline Drive<br>Coral Bay QLD 4571</p>
    <div class="web-tab">www.tarrowin.com.au</div>
    <div class="band"></div>
  </section>

  <section class="piece letterhead">
    <div class="brand">
      <span class="brand-dot"></span>
      <span class="brand-name">TARROWIN</span>
    </div>
    <p class="contact">
      Level 3, 14 Harbourline Drive, Coral Bay QLD 4571<br>
      <b>T:</b> (07) 5520 1184 · <b>F:</b> (07) 5520 1185 · <b>E:</b> info@tarrowin.com.au
    </p>
    <div class="web-tab">www.tarrowin.com.au</div>
    <div class="band"></div>
  </section>

  <section class="piece card-front">
    <div class="holder">
      <p class="holder-name">MORGAN ELLERY</p>
      <p class="holder-title">Manager</p>
    </div>
    <div class="brand">
      <span class="brand-dot"></span>
      <span class="brand-name">TARROWIN</span>
    </div>
    <div class="details">
      <p>T: (07) 5520 1184</p>
      <p>F: (07) 5520 1185</p>
      <p>M: 0412 336 907</p>
      <p>E: info@tarrowin.com.au</p>
      <div class="gap"></div>
      <p>Level 3, 14 Harbourline Drive</p>
      <p>Coral Bay QLD 4571</p>
    </div>
    <div class="web-tab">www.tarrowin.com.au</div>
    <div class="band"></div>
  </section>

  <section class="piece card-back">
    <div class="brand">
      <span class="brand-dot"></span>
      <span class="brand-name">TARROWIN</span>
    </div>
    <div class="services">
      <ul><li>· Electrical</li><li>· Fabrication</li><li>· Fitting</li></ul>
      <ul><li>· Labour Hire</li><li>· Plumbing</li><li>· Rigging</li></ul>
      <ul><li>· Shutdowns</li><li>· Boilermaking</li><li>· Carpentry</li></ul>
      <ul><li>· Concrete</li><li>· Construction</li><li>· Cranes</li></ul>
    </div>
  </section>

</body>
</html>
```